Gin Bottle label design

A label for three Gins, 1 Apple flavoured, 1 Bilberry flavoured and one London Dry Gin. All need to incorporate the business logo that i've attached along with the bottle we intend to use. The gin is 40% and will be in a 70cl bottle

```html
<!DOCTYPE html>
<html lang="en">
<head>
<meta charset="utf-8">
<title>Gin Label Range</title>
<link rel="stylesheet" href="https://fonts.googleapis.com/css2?family=Bebas+Neue&family=Oswald:wght@300;400&display=swap">
<style>
  :root {
    --page: #eef1f3;
    --silver: #c8c9cb;
    --silver-edge: #b7b8ba;
    --ink: #dcdddf;
    --apple: #2f8a3f;
    --apple-light: #3fa04e;
    --apple-band: #1f5a45;
    --bilberry: #4c2880;
    --bilberry-light: #6a46a8;
    --bilberry-band: #3b1d62;
    --london: #1f3ba6;
    --london-light: #3552c0;
    --london-band: #1a2d82;
  }
  * { box-sizing: border-box; margin: 0; padding: 0; }
  html, body { width: 1200px; height: 776px; overflow: hidden; }
  body {
    background: var(--page);
    display: flex;
    align-items: center;
    justify-content: center;
    gap: 64px;
  }
  .label {
    width: 300px;
    height: 500px;
    background: var(--silver);
    border: 1px solid var(--silver-edge);
    padding: 16px 14px 22px;
  }
  .label-face {
    position: relative;
    width: 100%;
    height: 100%;
    display: flex;
    flex-direction: column;
  }
  .pattern-field {
    position: relative;
    flex: 1;
  }
  .label--apple .pattern-field { background: radial-gradient(circle at 40% 35%, var(--apple-light), var(--apple) 70%); }
  .label--bilberry .pattern-field { background: radial-gradient(circle at 40% 35%, var(--bilberry-light), var(--bilberry) 70%); }
  .label--london .pattern-field { background: radial-gradient(circle at 40% 35%, var(--london-light), var(--london) 70%); }
  .brand {
    position: absolute;
    top: 62px;
    left: 0;
    right: 0;
    display: flex;
    align-items: center;
    justify-content: center;
    gap: 8px;
    color: var(--ink);
    font-family: "Bebas Neue", sans-serif;
    font-size: 24px;
    letter-spacing: 1px;
  }
  .brand-dot {
    width: 12px;
    height: 12px;
    border-radius: 50%;
    background: var(--ink);
  }
  .product {
    position: absolute;
    top: 190px;
    left: 0;
    right: 0;
    text-align: center;
    color: var(--ink);
    font-family: "Bebas Neue", sans-serif;
  }
  .product-variety {
    font-size: 34px;
    line-height: 1;
    letter-spacing: 1px;
  }
  .product-type {
    font-size: 158px;
    line-height: 0.85;
    letter-spacing: 2px;
  }
  .info-band {
    height: 52px;
    display: flex;
    align-items: center;
    justify-content: space-between;
    padding: 0 18px 0 22px;
    color: var(--ink);
    font-family: "Oswald", sans-serif;
    font-weight: 300;
    font-size: 15px;
    border-top: 1px solid rgba(255,255,255,0.35);
  }
  .label--apple .info-band { background: var(--apple-band); }
  .label--bilberry .info-band { background: var(--bilberry-band); }
  .label--london .info-band { background: var(--london-band); }
</style>
</head>
<body>

  <section class="label label--apple">
    <div class="label-face">
      <div class="pattern-field" role="img" aria-label="Green paisley and mandala line pattern">
        <div class="brand"><span class="brand-dot"></span><span class="brand-name">The Olive Table</span></div>
        <div class="product">
          <div class="product-variety">Apple</div>
          <div class="product-type">Gin</div>
        </div>
      </div>
      <div class="info-band"><span>40% alc. / Vol.</span><span>750 mL</span></div>
    </div>
  </section>

  <section class="label label--bilberry">
    <div class="label-face">
      <div class="pattern-field" role="img" aria-label="Purple paisley and mandala line pattern">
        <div class="brand"><span class="brand-dot"></span><span class="brand-name">The Olive Table</span></div>
        <div class="product">
          <div class="product-variety">Bilberry</div>
          <div class="product-type">Gin</div>
        </div>
      </div>
      <div class="info-band"><span>40% alc. / Vol.</span><span>750 mL</span></div>
    </div>
  </section>

  <section class="label label--london">
    <div class="label-face">
      <div class="pattern-field" role="img" aria-label="Blue paisley and mandala line pattern">
        <div class="brand"><span class="brand-dot"></span><span class="brand-name">The Olive Table</span></div>
        <div class="product">
          <div class="product-variety">London Dry</div>
          <div class="product-type">Gin</div>
        </div>
      </div>
      <div class="info-band"><span>40% alc. / Vol.</span><span>750 mL</span></div>
    </div>
  </section>

</body>
</html>
```